Home page design for a live auction website.

Hi, we are looking at finding a good design for an auction website, only home page .. We will not be selling anything online, so the website will only be a portal where visitors can check about our company, upcoming auctions, online catalogues etc.
See attached our logo. Please use the same red that you see on the logo in the designs that you provide.
The final design should communicate high-end auction website, as we will be selling expensive piece of arts and antiques.
We should have a main frame where images of arts will circulate, with description of the art piece. just like on http://paris.vellmarotte-quisande.com/
(but with a better design overall) and of course a menu with different tabs, like "about us", "previous sales" "next sales", "contact" , "how to buy", "meet our specialists".

Target Market(s)

High end segment, who can afford to pay up to 250'000 for a piece of art

Industry/Entity Type

Online

Number of Pages Required

1 page

Requirements
Must have
• a frame with images rotating, just like on http://paris.vellmarotte-quisande.com/ . but the rest of the design should be more refined.
• we should also have a strong call to action, "Free online estimation", click here, estimation delivered in 48 hours"
Nice to have
• Tremaux Auctions, the brand should be well visible

```html
<!DOCTYPE html>
<html lang="en">
<head>
<meta charset="utf-8">
<title>Tremaux Auctions — Home</title>
<link rel="stylesheet" href="https://fonts.googleapis.com/css2?family=Open+Sans:wght@300;400;600;700&display=swap">
<style>
:root{
  --brand-red:#c1272d;
  --brand-red-dark:#a31f24;
  --ink:#3a3a3a;
  --muted:#9a9a9a;
  --rule:#d6d6d6;
  --paper:#ffffff;
  --mist:#ececec;
}
*{box-sizing:border-box;margin:0;padding:0}
html,body{width:1200px;height:3300px;overflow:hidden;background:var(--paper)}
body{font-family:"Open Sans",Arial,sans-serif;color:var(--ink);position:relative}
.abs{position:absolute}

/* header */
.brand{left:0;width:1200px;top:62px;text-align:center}
.brand-name{font-size:26px;font-weight:600;color:var(--brand-red);letter-spacing:1px}
.brand-line{display:block;width:60px;height:2px;background:var(--brand-red);margin:10px auto 0}

.hero{left:0;top:200px;width:1200px;height:320px;
  background:linear-gradient(115deg,#7e1015 0%,#c1272d 14%,#e8584a 26%,#b3262a 34%,#f0b7ae 46%,#f7ebe8 58%,#f5f1f0 70%,#e9a59c 82%,#c7302c 92%,#8e151a 100%);
  box-shadow:inset 0 0 80px rgba(80,0,0,.35)}
.main-nav{left:200px;top:248px;width:800px;height:52px;background:rgba(255,255,255,.86);
  display:flex;justify-content:space-around;align-items:center}
.main-nav a{font-size:11px;font-weight:600;color:var(--ink);text-decoration:none;text-transform:uppercase;
  padding:0 14px;border-left:1px solid #bbb}
.main-nav a:first-child{border-left:none}
.hero-band{left:200px;top:436px;width:800px;height:64px;background:rgba(255,255,255,.3);
  display:flex;align-items:center;justify-content:space-between;padding:0 24px 0 20px}
.hero-title{font-size:30px;font-weight:700;color:#fff;letter-spacing:1px;text-transform:uppercase;
  text-shadow:0 1px 3px rgba(0,0,0,.25)}
.hero-btn{font-size:13px;color:#fff;padding:12px 26px;background:rgba(193,39,45,.55);border:1px solid rgba(255,255,255,.7)}

/* slider */
.slider{left:292px;top:580px;width:616px;height:308px;
  background:linear-gradient(90deg,#4f6d7e 0%,#8fa6ad 18%,#c8c2ad 34%,#6f7f86 48%,#e6e1d6 56%,#d6cfc2 70%,#3b3833 82%,#bcb3a3 92%,#7a6f62 100%);
  box-shadow:inset 0 0 40px rgba(0,0,0,.25)}
.slider-caption{left:292px;top:812px;width:616px;height:52px;background:rgba(40,40,40,.72);
  color:#eee;font-size:11px;line-height:17px;padding:9px 20px 0 60px}
.caption-dot{left:302px;top:825px;width:26px;height:26px;border-radius:50%;background:var(--brand-red)}
.read-more{left:808px;top:864px;width:100px;height:30px;background:var(--brand-red);color:#fff;font-size:12px;
  display:flex;align-items:center;justify-content:center}
.arrow{top:692px;width:28px;height:56px;background:var(--brand-red);display:flex;align-items:center;justify-content:center}
.thumbs{left:208px;top:944px;width:784px;height:88px;display:flex;gap:6px}
.thumbs div{flex:1;box-shadow:inset 0 0 16px rgba(0,0,0,.3)}

/* section heads */
.section-label{left:0;width:1200px;text-align:center;font-size:11px;color:var(--muted);text-transform:uppercase;letter-spacing:1px}
.section-label span{background:var(--paper);padding:0 16px;position:relative}
.section-label::before{content:"";position:absolute;left:440px;right:440px;top:8px;height:1px;background:var(--rule)}
.section-label.on-mist span{background:#dedede}
.section-title{left:0;width:1200px;text-align:center;color:var(--brand-red);font-weight:700;text-transform:uppercase}
.section-copy{text-align:center;color:var(--muted);font-size:13px;line-height:21px}

.about-quote{top:1176px;font-size:28px;line-height:40px}
.about-copy{left:290px;width:620px;top:1276px;text-align:justify;font-size:12px;line-height:19px}
.about-images{left:380px;top:1428px;width:440px;height:172px;display:flex;gap:4px}
.about-images div{flex:1;background:linear-gradient(160deg,#1e1e1e 0%,#6a6a6a 35%,#d4d4d4 55%,#4a4a4a 80%,#8a8a8a 100%)}

.how-to-buy{left:0;top:1640px;width:1200px;height:540px;
  background:linear-gradient(170deg,#b9b9b9 0%,#e4e4e4 18%,#cfcfcf 32%,#ececec 55%,#f6f6f6 75%,#fff 100%)}
.how-title{top:1846px;font-size:26px}
.how-copy{left:300px;width:600px;top:1900px;font-size:12px;line-height:18px}
.step{top:2008px;width:80px;height:80px;border-radius:50%;background:#fff;display:flex;align-items:center;justify-content:center;
  box-shadow:0 2px 8px rgba(0,0,0,.08)}
.step-arrow{top:2044px}
.free-badge{left:800px;top:1968px;width:160px;height:160px;border-radius:50%;background:#fff;border:6px solid #e4e4e4;
  display:flex;flex-direction:column;align-items:center;justify-content:center;line-height:1}
.free-badge .big{font-size:34px;font-weight:300;color:var(--ink)}
.free-badge .red{font-size:22px;font-weight:600;color:var(--brand-red)}
.free-badge .small{font-size:10px;font-weight:700;letter-spacing:1px;color:var(--ink);margin-top:4px}

.prev-title{top:2340px;font-size:26px}
.prev-copy{left:260px;width:680px;top:2388px;font-size:12px;line-height:18px}
.collage div{position:absolute}
.tile-brand{background:#fff;display:flex;align-items:center;justify-content:center;
  font-size:14px;font-weight:600;color:var(--brand-red)}

.contact-title{top:2990px;font-size:26px}
.contact-copy{left:520px;width:200px;top:3040px;text-align:left;font-size:11px;line-height:16px}
.contact-meta{left:520px;width:220px;top:3150px;font-size:11px;line-height:18px;color:var(--muted)}

.site-footer{left:0;top:3220px;width:1200px;height:80px;background:var(--brand-red);
  display:flex;justify-content:center;align-items:center;gap:46px}
.site-footer a{color:#f6d3d4;font-size:12px;text-decoration:none}
</style>
</head>
<body>

<header>
  <div class="abs brand"><span class="brand-name">Tremaux Auctions</span><span class="brand-line"></span></div>
  <div class="abs hero" role="img" aria-label="Photograph of red autumn maple leaves"></div>
  <nav class="abs main-nav">
    <a href="#">About us</a><a href="#">Previous sales</a><a href="#">Next sales</a>
    <a href="#">Contact</a><a href="#">How to buy</a><a href="#">Meet our specialists</a>
  </nav>
  <div class="abs hero-band"><h1 class="hero-title">A source of good design</h1><span class="hero-btn">See more</span></div>
</header>

<section class="featured">
  <div class="abs slider" role="img" aria-label="Featured artwork: painted panels with a stylised animal figure"></div>
  <div class="abs slider-caption">Oil on canvas, signed lower right, from a private Swiss collection, presented in our spring sale of modern art.</div>
  <div class="abs caption-dot"></div>
  <div class="abs read-more">Read more</div>
  <div class="abs arrow" style="left:216px"><svg width="10" height="14"><path d="M8 1 2 7l6 6" fill="none" stroke="#fff" stroke-width="2"/></svg></div>
  <div class="abs arrow" style="left:956px"><svg width="10" height="14"><path d="M2 1l6 6-6 6" fill="none" stroke="#fff" stroke-width="2"/></svg></div>
  <div class="abs thumbs">
    <div role="img" aria-label="Artwork thumbnail" style="background:linear-gradient(135deg,#2b1d4a,#7a4fa0,#d9a0c8)"></div>
    <div role="img" aria-label="Artwork thumbnail" style="background:linear-gradient(135deg,#e5b03a,#c44a2e,#5a1a12)"></div>
    <div role="img" aria-label="Artwork thumbnail" style="background:linear-gradient(135deg,#0f2b45,#2f6f9a,#e0c46a)"></div>
    <div role="img" aria-label="Artwork thumbnail" style="background:linear-gradient(135deg,#3a2a1a,#b79a6a,#f0e0c0)"></div>
    <div role="img" aria-label="Artwork thumbnail" style="background:linear-gradient(135deg,#2a2a2a,#9a9a9a,#e6e6e6)"></div>
    <div role="img" aria-label="Artwork thumbnail" style="background:linear-gradient(135deg,#f2c4cc,#d07c86,#6a1f2a)"></div>
    <div role="img" aria-label="Artwork thumbnail" style="background:linear-gradient(135deg,#e8d6a0,#a23a3a,#2a0e10)"></div>
    <div role="img" aria-label="Artwork thumbnail" style="background:linear-gradient(135deg,#f2ece2,#c9b8a0,#6e5a44)"></div>
  </div>
</section>

<section class="about">
  <div class="abs section-label" style="top:1112px"><span>About us</span></div>
  <h2 class="abs section-title about-quote">“Art is not what you see,<br>but what you make others to see”</h2>
  <p class="abs section-copy about-copy">Since our founding, Tremaux Auctions has brought fine art, antiques and rare objects to collectors who value provenance and care. Each piece is examined by our specialists, researched in depth and presented with a clear catalogue note. We hold live sales throughout the year and publish every catalogue online, so that buyers near and far can follow each lot, ask questions and prepare their bids with confidence.</p>
  <div class="abs about-images">
    <div role="img" aria-label="Black and white photograph of hands"></div>
    <div role="img" aria-label="Black and white photograph of hands"></div>
    <div role="img" aria-label="Black and white photograph of hands"></div>
  </div>
</section>

<section>
  <div class="abs how-to-buy" role="img" aria-label="Faint grey ink-wash background"></div>
  <div class="abs section-label on-mist" style="top:1756px"><span>How to buy</span></div>
  <h2 class="abs section-title how-title">Estimation delivered in 48 hours !</h2>
  <p class="abs section-copy how-copy">Send us a few photographs and a short description of your piece. Our specialists study every request and return a free estimate of its value within two working days.</p>
  <div class="abs step" style="left:248px"><svg width="34" height="34" viewBox="0 0 34 34" fill="none" stroke="#c1272d" stroke-width="2"><path d="M12 18V8a2 2 0 0 1 4 0v9M16 16v-3a2 2 0 0 1 4 0v4M20 17v-2a2 2 0 0 1 4 0v6c0 5-3 9-8 9s-7-3-9-7l-2-4a2 2 0 0 1 3-2l3 3"/></svg></div>
  <svg class="abs step-arrow" style="left:350px" width="40" height="10"><path d="M0 5h36M31 1l5 4-5 4" fill="none" stroke="#555" stroke-width="1.5"/></svg>
  <div class="abs step" style="left:440px"><svg width="30" height="34" viewBox="0 0 30 34" fill="none" stroke="#c1272d" stroke-width="2"><path d="M5 2h14l7 7v23H5zM19 2v7h7M10 16h10M10 21h10M10 26h6"/></svg></div>
  <svg class="abs step-arrow" style="left:542px" width="40" height="10"><path d="M0 5h36M31 1l5 4-5 4" fill="none" stroke="#555" stroke-width="1.5"/></svg>
  <div class="abs step" style="left:632px"><svg width="32" height="32" viewBox="0 0 32 32" fill="none" stroke="#c1272d" stroke-width="2"><path d="M8 3l5 6-3 3c1 4 5 8 9 9l3-3 6 5-3 4C14 27 5 18 4 6z"/></svg></div>
  <svg class="abs step-arrow" style="left:734px" width="40" height="10"><path d="M0 5h36M31 1l5 4-5 4" fill="none" stroke="#555" stroke-width="1.5"/></svg>
  <div class="abs free-badge"><span class="big">FREE</span><span class="red">ONLINE</span><span class="small">ESTIMATION</span></div>
</section>

<section>
  <div class="abs section-label" style="top:2266px"><span>Previous sale</span></div>
  <h2 class="abs section-title prev-title">Previous sale</h2>
  <p class="abs section-copy prev-copy">Browse the results of our recent sales, from old master drawings to modern sculpture, with the prices realised for each lot.</p>
  <div class="collage">
    <div role="img" aria-label="Black and white portrait photograph" style="left:180px;top:2492px;width:210px;height:168px;background:linear-gradient(150deg,#1a1a1a 0%,#5e5e5e 30%,#d8d8d8 55%,#7a7a7a 80%,#2e2e2e 100%)"></div>
    <div class="tile-brand" style="left:390px;top:2492px;width:210px;height:168px">Tremaux Auctions</div>
    <div role="img" aria-label="Poster with large design lettering" style="left:600px;top:2492px;width:210px;height:168px;background:linear-gradient(180deg,#ffffff 0%,#f0f0f0 40%,#6a6a6a 70%,#262626 100%)"></div>
    <div role="img" aria-label="Mosaic of small colourful photographs" style="left:180px;top:2660px;width:210px;height:168px;background:linear-gradient(135deg,#1f3f5a 0%,#3f7ca8 25%,#c26a4a 50%,#e0c27a 70%,#6a3a5a 100%)"></div>
    <div role="img" aria-label="Sketch of a seated figure" style="left:390px;top:2660px;width:210px;height:168px;background:linear-gradient(180deg,#fafafa,#e2e2e2 60%,#b8b8b8)"></div>
    <div role="img" aria-label="Architectural photograph of a tower" style="left:600px;top:2660px;width:210px;height:168px;background:linear-gradient(180deg,#c4d6e4 0%,#7f9bb2 40%,#3a4c5e 75%,#1e2832 100%)"></div>
    <div role="img" aria-label="Photograph of a curved modern building" style="left:810px;top:2492px;width:210px;height:336px;background:linear-gradient(160deg,#f0f0f0 0%,#a8a8a8 30%,#3c3c3c 55%,#bdbdbd 75%,#2a2a2a 100%)"></div>
  </div>
</section>

<section>
  <div class="abs section-label" style="top:2914px"><span>Contact</span></div>
  <h2 class="abs section-title contact-title">Contact us</h2>
  <p class="abs section-copy contact-copy">Our team is happy to answer your questions about buying, selling or visiting one of our upcoming sales. Write to us or call during opening hours.</p>
  <p class="abs contact-meta">Tel. +41 22 310 45 80<br>info@tremaux-auctions.com</p>
</section>

<footer class="abs site-footer">
  <a href="#">About Us</a><a href="#">Previous Sales</a><a href="#">Next Sales</a>
  <a href="#">Contact</a><a href="#">How to buy</a><a href="#">How to Buy/Sell to Buy</a>
</footer>

</body>
</html>
```